Pelton|Marsh & Quillan business card contest

We need a logo for an upscale boutique diversified company involved in real estate, investments, cattle, and more. Our businesses DO NOT need to be reflected in the business card nor do we want them noted. This is our logo and colors and we love our logo and colors. Our logo looks best against a black background and we like to include the firm name in our logo usage. importantly, the names Pelton and Marsh are separated by | not / and we use an ampersand not the word and.
On the front of the card, we want to include:
company logo and name (Pelton|Marsh & Quillan)
on the back, we would definitely include:
address, email, cell #
logo and name (smaller size than front)

The variable will be location of individual name and title (mine for example is ) - whether on the front OR on the back. interested in variations from which to choose
Dr. Neil R. Whitcombe, CFA
Scientifique des Fusées Financières

we would like to use contemporary symbols for address, email address, cell # with an option for web site that we do not intend to use initially. we like two sided cards and believe this design should use four rounded corners with the standard size. we prefer thicker card stock and may look at metal.

```html
<!DOCTYPE html>
<html lang="en">
<head>
<meta charset="utf-8">
<title>Pelton|Marsh &amp; Quillan — Business Card</title>
<link href="https://fonts.googleapis.com/css2?family=Roboto:wght@400;500&display=swap" rel="stylesheet">
<style>
  :root {
    --page-bg: #e2e2e2;
    --card-bg: #0d0d0d;
    --accent: #e8822a;
    --text-grey: #8c8c8c;
    --brand-grey: #7d7d7d;
    --stripe-grey: #5e5e5e;
    --tick-grey: #3a3a3a;
  }
  * { margin: 0; padding: 0; box-sizing: border-box; }
  html, body { width: 1200px; height: 1200px; overflow: hidden; }
  body {
    background: var(--page-bg);
    font-family: "Roboto", Arial, sans-serif;
    position: relative;
  }
  .card {
    position: absolute;
    left: 240px;
    width: 720px;
    height: 420px;
    background: var(--card-bg);
  }
  .card--front { top: 142px; }
  .card--back { top: 636px; }

  /* Front brand lockup */
  .brand-front {
    position: absolute;
    left: 0; right: 0; top: 118px;
    display: flex;
    flex-direction: column;
    align-items: center;
  }
  .brand-square {
    width: 62px; height: 62px;
    background: var(--accent);
  }
  .brand-name {
    color: var(--brand-grey);
    font-weight: 400;
    white-space: nowrap;
  }
  .brand-front .brand-name { font-size: 38px; margin-top: 34px; letter-spacing: 0.5px; }

  /* Back brand lockup */
  .brand-back {
    position: absolute;
    right: 27px; top: 28px;
    display: flex;
    flex-direction: column;
    align-items: flex-end;
  }
  .brand-back .brand-square { width: 44px; height: 44px; margin-right: 92px; }
  .brand-back .brand-name { font-size: 24px; margin-top: 28px; }

  /* Person */
  .person { position: absolute; left: 27px; top: 186px; }
  .person__name {
    color: var(--accent);
    font-weight: 500;
    font-size: 23px;
    line-height: 28px;
  }
  .person__title {
    color: var(--text-grey);
    font-size: 17px;
    line-height: 22px;
    margin-top: 5px;
  }

  /* Contacts */
  .contacts { position: absolute; left: 27px; top: 296px; list-style: none; }
  .contacts li {
    display: flex; align-items: center;
    height: 26.5px;
    color: var(--text-grey);
    font-size: 17px;
  }
  .contacts svg { width: 15px; height: 15px; margin-right: 9px; fill: var(--accent); }

  .address {
    position: absolute; right: 27px; top: 322px;
    text-align: right;
    color: var(--text-grey);
    font-size: 17px;
    line-height: 26.5px;
    font-style: normal;
  }

  /* Bottom band */
  .band-ticks {
    position: absolute; left: 0; top: 393px;
    width: 437px; height: 10px;
    background: var(--tick-grey);
  }
  .band-accent {
    position: absolute; left: 0; bottom: 0;
    width: 437px; height: 10px;
    background: var(--accent);
  }
  .band-stripes {
    position: absolute; left: 437px; bottom: 0;
    width: 283px; height: 27px;
    background: var(--stripe-grey);
  }
</style>
</head>
<body>

  <section class="card card--front" aria-label="Card front">
    <div class="brand-front">
      <div class="brand-square"></div>
      <div class="brand-name">Pelton|Marsh &amp; Quillan</div>
    </div>
  </section>

  <section class="card card--back" aria-label="Card back">
    <div class="brand-back">
      <div class="brand-square"></div>
      <div class="brand-name">Pelton|Marsh &amp; Quillan</div>
    </div>

    <div class="person">
      <h1 class="person__name">Dr. Neil R. Whitcombe, CFA</h1>
      <p class="person__title">Scientifique des Fusées Financières</p>
    </div>

    <ul class="contacts">
      <li>
        <svg viewBox="0 0 24 24" aria-hidden="true"><path d="M6.6 10.8c1.4 2.8 3.8 5.1 6.6 6.6l2.2-2.2c.3-.3.7-.4 1-.2 1.1.4 2.3.6 3.6.6.6 0 1 .4 1 1V20c0 .6-.4 1-1 1C10.6 21 3 13.4 3 4c0-.6.4-1 1-1h3.5c.6 0 1 .4 1 1 0 1.3.2 2.5.6 3.6.1.3 0 .7-.2 1L6.6 10.8z"/></svg>
        +0044-7946-0381
      </li>
      <li>
        <svg viewBox="0 0 24 24" aria-hidden="true"><path d="M2 5h20v14H2z M4 7v.5l8 5 8-5V7l-8 5z" fill-rule="evenodd"/></svg>
        info@peltonmarsh.com
      </li>
      <li>
        <svg viewBox="0 0 24 24" aria-hidden="true"><circle cx="12" cy="12" r="10"/></svg>
        www.peltonmarsh.com
      </li>
    </ul>

    <address class="address">
      P.O. Box: 418, Alder Lane<br>
      552/ Bristol, United Kingdom
    </address>

    <div class="band-ticks" role="img" aria-label="Row of small grey tick marks"></div>
    <div class="band-accent"></div>
    <div class="band-stripes" role="img" aria-label="Grey vertical stripe pattern"></div>
  </section>

</body>
</html>
```